VELMIT Business Card

VELMIT (www.velmitpools.example) is a veteran in the swimming pool maintenance and repair business..we have served our clients for 15 years and have a research chemist, an electrician, a plumber and a pool building contractor (in part) on staff...We want to provide a business card that has a dual purpose, that people want to keep around, that leaves people speechless in the sense that they understand the mission of and the experience level of the TEAM at VELMIT.

Target Market(s)

persons who enjoy swimming and make it a priority to swim

Industry/Entity Type

Building

Font styles to use
Serif
Sans Serif

Colors
85acd3
3176b5
95b6d8
3276b5
0355a3
0555a3
0255a3
0455a3
85abd2

Requirements
Must have
• name, title, address, email, text
Nice to have
• a die cut shape
Should not have
• cartoons, pictures of pools

```html
<!DOCTYPE html>
<html lang="en">
<head>
<meta charset="utf-8">
<title>VELMIT Business Card</title>
<link rel="stylesheet" href="https://fonts.googleapis.com/css2?family=Josefin+Sans:wght@300;400;600;700&family=Montserrat:wght@300;400;500;600;700;800&display=swap">
<style>
  :root {
    --page-bg: #eef1f5;
    --card-blue: #7ba4d8;
    --card-white: #ffffff;
    --brand-blue: #3276b5;
    --navy: #1c3563;
    --icon-blue: #3276b5;
    --ink: #111111;
    --bubble: #e9eef4;
  }
  * { box-sizing: border-box; margin: 0; padding: 0; }
  html, body { width: 1200px; height: 1000px; overflow: hidden; }
  body {
    background: var(--page-bg);
    font-family: "Montserrat", sans-serif;
    position: relative;
  }
  .card {
    position: absolute;
    left: 250px;
    width: 700px;
    height: 400px;
    border-radius: 16px 90px 16px 90px;
    overflow: hidden;
    box-shadow: 0 8px 24px rgba(20, 40, 70, 0.18);
  }
  /* ---------- front ---------- */
  .card--front { top: 60px; background: var(--card-blue); }
  .front-brand {
    position: absolute; right: 62px; top: 62px; text-align: center; color: #fff;
  }
  .front-brand__name {
    font-family: "Montserrat", sans-serif; font-weight: 600;
    font-size: 46px; letter-spacing: 2px; line-height: 1;
  }
  .front-brand__tagline {
    font-family: "Montserrat", sans-serif; font-weight: 600;
    font-size: 12px; letter-spacing: 1.5px; margin-top: 10px;
  }
  .holder { position: absolute; left: 52px; top: 178px; }
  .holder__name {
    font-family: "Josefin Sans", sans-serif; font-weight: 600;
    font-size: 38px; color: var(--ink); line-height: 1;
  }
  .holder__rule { width: 185px; height: 2px; background: #fff; margin-top: 6px; }
  .holder__title {
    font-family: "Josefin Sans", sans-serif; font-weight: 300;
    font-size: 30px; color: #fff; margin-top: 4px; padding-left: 6px;
  }
  .contact {
    position: absolute; left: 360px; top: 272px; list-style: none;
    font-family: "Josefin Sans", sans-serif; font-size: 22px; color: var(--ink);
  }
  .contact li { display: flex; align-items: center; gap: 8px; height: 27px; }
  .contact svg { width: 20px; height: 20px; flex: none; }
  /* ---------- back ---------- */
  .card--back { top: 540px; background: var(--card-white); display: flex; }
  .back-brand {
    width: 320px; display: flex; flex-direction: column;
    align-items: center; justify-content: center;
  }
  .back-brand__name {
    font-weight: 600; font-size: 64px; color: var(--brand-blue);
    line-height: 1; letter-spacing: 2px;
  }
  .back-brand__tagline {
    font-weight: 600; font-size: 16px; letter-spacing: 1.6px; color: var(--brand-blue);
    margin-top: 14px;
  }
  .senses {
    flex: 1; background: var(--card-blue); position: relative;
    padding: 38px 28px 0 26px;
  }
  .senses__heading {
    font-weight: 800; font-size: 30px; color: var(--navy);
    text-align: center; letter-spacing: 0.5px; line-height: 1;
  }
  .senses__sub {
    display: flex; align-items: center; justify-content: center; gap: 6px;
    font-weight: 400; font-size: 20px; color: var(--navy); letter-spacing: 1px;
    margin-top: 4px;
  }
  .senses__sub::before, .senses__sub::after {
    content: ""; width: 40px; border-top: 2px dotted var(--navy); opacity: .7;
  }
  .senses__list { list-style: none; margin-top: 20px; }
  .senses__item { display: flex; align-items: center; gap: 14px; height: 54px; }
  .senses__bubble {
    width: 42px; height: 42px; border-radius: 50%; flex: none;
    background: radial-gradient(circle at 35% 30%, #ffffff, var(--bubble) 60%, #b9c7d8);
  }
  .senses__text { font-size: 14.5px; color: var(--navy); line-height: 1.2; letter-spacing: .4px; }
  .senses__text strong { display: block; font-weight: 700; }
  .senses__url {
    position: absolute; left: 16px; right: 14px; bottom: 26px; height: 24px;
    background: var(--navy); color: #fff; font-size: 12px; font-weight: 600;
    display: flex; align-items: center; justify-content: center; letter-spacing: .4px;
  }
</style>
</head>
<body>

  <section class="card card--front" aria-label="Business card front">
    <div class="front-brand">
      <div class="front-brand__name">VELMIT</div>
      <div class="front-brand__tagline">POOL CARE, DONE RIGHT</div>
    </div>

    <div class="holder">
      <div class="holder__name">Your Name</div>
      <div class="holder__rule"></div>
      <div class="holder__title">Manager</div>
    </div>

    <ul class="contact">
      <li>
        <svg viewBox="0 0 20 20" aria-hidden="true"><circle cx="10" cy="10" r="8.5" fill="none" stroke="#3276b5" stroke-width="1.6"/><path d="M7 5.5c-.8.6-1 1.8-.4 3.2.8 1.9 2.5 3.7 4.3 4.6 1.3.6 2.5.5 3.1-.3l-1.6-1.6-1.3.7c-1-.5-2-1.5-2.5-2.5l.7-1.3z" fill="#3276b5"/></svg>
        your phone number
      </li>
      <li>
        <svg viewBox="0 0 20 20" aria-hidden="true"><rect x="2" y="5" width="16" height="11" rx="1" fill="#3276b5"/><path d="M2.5 5.5 10 11l7.5-5.5" fill="none" stroke="#7ba4d8" stroke-width="1.3"/></svg>
        your email@mailbox.example
      </li>
      <li>
        <svg viewBox="0 0 20 20" aria-hidden="true"><path d="M10 2 1.5 10h2.5v8h4.5v-5h3v5H16v-8h2.5z" fill="#3276b5"/></svg>
        your address stret
      </li>
    </ul>
  </section>

  <section class="card card--back" aria-label="Business card back">
    <div class="back-brand">
      <div class="back-brand__name">VELMIT</div>
      <div class="back-brand__tagline">POOL CARE, DONE RIGHT</div>
    </div>

    <div class="senses">
      <h2 class="senses__heading">USE YOUR SENSES</h2>
      <div class="senses__sub">AT THE POOL</div>
      <ul class="senses__list">
        <li class="senses__item"><span class="senses__bubble" role="img" aria-label="Eye icon"></span><span class="senses__text">LOOK FOR WATER THAT’S<strong>CLEAN, CLEAR AND BLUE</strong></span></li>
        <li class="senses__item"><span class="senses__bubble" role="img" aria-label="Hand icon"></span><span class="senses__text">CHECK FOR TILES THAT FEEL<strong>SMOOTH AND CLEAN</strong></span></li>
        <li class="senses__item"><span class="senses__bubble" role="img" aria-label="Nose icon"></span><span class="senses__text">MAKE SURE THERE ARE<strong>NO STRONG ODORS</strong></span></li>
        <li class="senses__item"><span class="senses__bubble" role="img" aria-label="Ear icon"></span><span class="senses__text">LISTEN FOR POOL<strong>CLEANING EQUIPMENT</strong></span></li>
      </ul>
      <div class="senses__url">SwimWellGuide.example</div>
    </div>
  </section>

</body>
</html>
```